Webdesign für einen Softwarehersteller
Zielgruppe
Wir sind Softwarehersteller einer Arbeitsschutz Management Software. Unser Leistungsumfang beträgt
a) die Analyse, Beurteilung und Risikoeinschätzung von Gefährdungen an einem Arbeitsplatz, einer Maschine oder Tätigkeit
b) die Unterweisung von Mitarbeitern
c) ein Risiko- und Maßnahmenmanagement
d) ein Unfallmanagement bei welchem Unfälle erfasst, ausgewertet und präventive Maßnahmen ergriffen werden
e) ein Management zur Verwaltung von Gefahrstoffen inkl. der Ableitung von präventiven Maßnahmen
f) ein Tool zur Auditierung von Prozessen, wie z.B. ISO-Normen
Unsere Zielgruppe sind Industrieunternehmen ab 500 Mitarbeitern. Der Traumkunde hat 4000 - 8000 Mitarbeiter. Unsere Software ist multilingual und kann auch weltweit eingesetzt werden womit auch weltweit operierende Konzerne zu unserer Zielgruppe gehören.
Mit unserer Software dokumentiert das Unternehmen alle notwendigen Prozesse zur Einhaltung des Arbeitsschutzes. Die Software unterstützt dabei das Unternehmen, die Menschen im Unternehmen best möglich zu schützen und allen rechtlichen Anforderungen gerecht zu werden.
Aufgabenstellung
Hallo Designer:innen,
zuerst möchte ich mich bei euch bedanken, dass Ihr euch an unserem Projekt beteiligt. Wir suchen eine Homepage, sehr clean, sehr modern und passend zu einem Softwareprodukt z.B. https://brennlaub.com/seiten-vorlagen (Kalvorix Theme). Wir legen Wert auf Struktur, Übersichtlichkeit, Modern.
Textinhalte findet Ihr auf der bestehenden Homepage.
WICHTIG!!!
a) Die bestehende Homepage dient als Inhaltsvorlage. Wir finden die Homepage nicht gut!
b) Wir erwarten, ein Hochwertiges Design sowie eine durchdachte Aufteilung der Homepage. Wenn Ihr z.B. der Meinung seid, dass auf der Landingpage eine Produktgallerie mit Bildern notwendig ist, dann fügt diese bitte ein und verwendet Demo-Bilder. Wir liefern gerne später Inhalte für die Bereiche. Die neue Webseite darf gerne von der bestehenden Struktur abweichen.
c) Selvadon wird ein neues, moderneres Logo erhalten. Das neue Logo findet Ihr unter
https://stage.selvadon.de/wp-content/uploads/2022/02/test_logo1.png
https://stage478.selvadon.de/wp-content/uploads/2022/03/Logo_web.png

```html
<!DOCTYPE html>
<html lang="de">
<head>
<meta charset="utf-8">
<title>Selvadon – Software für Arbeitsschutz</title>
<link href="https://fonts.googleapis.com/css2?family=Lato:wght@300;400;700;900&display=swap" rel="stylesheet">
<style>
:root{
  --green:#6cb33f;
  --green-dark:#4f9a2a;
  --hero-a:#d6eccb;
  --hero-b:#b9ccb3;
  --ink:#333a30;
  --text:#4a4a4a;
  --muted:#777;
  --grey-band:#f1f1f1;
  --footer:#c6e4b6;
  --footer-bar:#4b5a40;
  --page:#ffffff;
}
*{margin:0;padding:0;box-sizing:border-box}
html,body{width:1200px;height:2948px;overflow:hidden;background:#fff}
body{font-family:'Lato',sans-serif;color:var(--text);position:relative}
.page{position:absolute;left:100px;top:115px;width:993px;height:2727px;background:var(--page);box-shadow:0 4px 24px rgba(0,0,0,.08);overflow:hidden}
.abs{position:absolute}
.hero-bg{position:absolute;left:0;top:0;width:993px;height:560px}
.brand{position:absolute;display:flex;align-items:center;gap:8px;font-weight:700;letter-spacing:3px;color:var(--ink)}
.brand .mark{width:14px;height:14px;background:var(--green)}
.nav a{position:absolute;top:53px;font-size:10px;font-weight:700;color:#3d3d3d;text-decoration:none;letter-spacing:.3px}
.nav a.active{color:var(--green);border-bottom:2px solid var(--green);padding-bottom:3px}
.contact-photo{position:absolute;left:740px;top:22px;width:68px;height:68px;border-radius:50%;background:radial-gradient(circle at 50% 40%,#e8e8e8,#b7b7b7);border:3px solid #fff}
.contact-name{position:absolute;right:80px;top:32px;text-align:right;font-size:10px;color:#444;line-height:13px}
.contact-name span{color:var(--muted)}
.btn{position:absolute;background:var(--green);color:#fff;font-weight:700;font-size:11px;letter-spacing:.3px;display:flex;align-items:center;justify-content:center;text-transform:uppercase}
.hero-title{position:absolute;left:130px;top:165px;font-size:61px;font-weight:700;line-height:54px;color:var(--ink);letter-spacing:-.5px}
.hero-sub{position:absolute;left:130px;top:290px;font-size:21px;line-height:25px;color:#333}
.link-more{position:absolute;left:263px;top:392px;font-size:11px;font-weight:700;color:#333}
.placeholder{position:absolute}
.eyebrow{position:absolute;font-size:13px;color:var(--green);letter-spacing:.4px;text-transform:uppercase}
.section-title{position:absolute;font-size:24px;color:#333;font-weight:400}
.center{left:0;width:993px;text-align:center}
.feature{position:absolute;left:567px;width:360px}
.feature .plus{position:absolute;left:0;top:-2px;width:19px;height:19px;border-radius:50%;background:var(--green);color:#fff;font-size:15px;line-height:19px;text-align:center;font-weight:700}
.feature h3{margin-left:21px;font-size:12px;font-weight:700;color:#333;margin-bottom:5px}
.feature p{margin-left:21px;font-size:11.5px;line-height:17px;color:#444}
.band{position:absolute;left:0;width:993px;background:var(--grey-band)}
.body-text{position:absolute;font-size:11.5px;line-height:17px;color:#444}
.module-list{position:absolute;list-style:none;font-size:11.5px;color:#444}
.module-list li{height:20.6px;padding-left:19px;position:relative}
.module-list li::before{content:"+";position:absolute;left:0;top:-2px;color:var(--green);font-size:15px;font-weight:700}
.client{position:absolute;top:1862px;transform:translateX(-50%);font-size:26px;font-weight:900;color:#1f2a44;display:flex;align-items:center;gap:8px;letter-spacing:.5px}
.client .sq{width:16px;height:16px;background:#1f2a44}
.client .dot{width:16px;height:16px;border-radius:50%;background:#1f2a44}
.footer{position:absolute;left:0;top:2428px;width:993px;height:240px;background:var(--footer)}
.footer-bar{position:absolute;left:0;top:2668px;width:993px;height:59px;background:var(--footer-bar);color:#e8efe3;font-size:10px}
.f-col{position:absolute;top:61px;font-size:11px;color:#3f4a38;line-height:16.6px}
.f-col h4{font-size:9.5px;font-weight:400;letter-spacing:.4px;color:#4b5a40;margin-bottom:11px}
</style>
</head>
<body>
<div class="page">

  <!-- Hero -->
  <svg class="hero-bg" viewBox="0 0 993 560" preserveAspectRatio="none" aria-hidden="true">
    <defs>
      <linearGradient id="heroGrad" x1="0" y1="0" x2="1" y2="0">
        <stop offset="0" stop-color="var(--hero-a)"/>
        <stop offset="1" stop-color="var(--hero-b)"/>
      </linearGradient>
    </defs>
    <path d="M0 0 H993 V430 C860 470 760 420 600 480 C430 545 200 560 0 515 Z" fill="url(#heroGrad)"/>
    <path d="M120 0 C60 160 150 420 380 520 C300 420 250 200 330 0 Z" fill="#ffffff" opacity=".12"/>
  </svg>

  <div class="brand" style="left:38px;top:30px;font-size:11px;flex-direction:column;gap:6px">
    <span class="mark" style="width:28px;height:28px"></span>
    <span>SELVADON</span>
  </div>

  <nav class="nav">
    <a class="active" style="left:284px">HOME</a>
    <a style="left:354px">SOFTWARE MODULE</a>
    <a style="left:494px">UNTERNEHMEN</a>
    <a style="left:611px">KONTAKT</a>
  </nav>

  <div class="contact-photo" role="img" aria-label="Porträtfoto des Ansprechpartners"></div>
  <div class="contact-name">Jonas Brenner<br><span>Ihr persönlicher Ansprechpartner</span></div>
  <div class="btn" style="left:826px;top:63px;width:119px;height:19px;font-size:9px">Termin vereinbaren</div>

  <h1 class="hero-title">Software für<br>Arbeitsschutz</h1>
  <p class="hero-sub">mit einer breiten Palette an<br>Modulen und Funktionen</p>
  <div class="btn" style="left:130px;top:380px;width:107px;height:40px">Entdecken</div>
  <div class="link-more">WARUM SELVADON ▶</div>

  <div class="placeholder" role="img" aria-label="Bildschirm mit der Arbeitsschutz-Software, Ansicht einer Gefahrstoffliste"
       style="left:583px;top:154px;width:329px;height:434px;background:linear-gradient(160deg,#2a2a2a 0%,#3a3a3a 55%,#e6e6e6 56%,#f4f4f4 100%);border-radius:6px;opacity:.95"></div>

  <!-- Vorteile -->
  <div class="eyebrow center" style="top:672px">Vorteile Ihres Geschäfts</div>
  <h2 class="section-title center" style="top:696px">Die Selvadon Arbeitsschutz Software</h2>

  <div class="placeholder" role="img" aria-label="Dashboard der Software mit Aufgabenliste und eingeblendeten Tabellen"
       style="left:42px;top:796px;width:470px;height:298px;background:linear-gradient(180deg,#ffffff 0%,#f3f5f2 60%,#e4ece0 100%);box-shadow:0 4px 16px rgba(0,0,0,.15)"></div>

  <div class="feature" style="top:787px"><span class="plus">+</span><h3>Vielseitige Entlastung</h3><p>Die Selvadon Arbeitsschutz Software entlastet alle Beteiligten im Arbeitsschutz. Angefangen bei den Vorgesetzten und Fachkräften für Arbeitssicherheit, über die Mitarbeiter mit Kontrollfunktionen bis hin zu den IT Administratoren.</p></div>
  <div class="feature" style="top:892px"><span class="plus">+</span><h3>Hohe Effizienz &amp; Shutz</h3><p>Selvadon besitzt eine Vielzahl an automatisierten Abläufen und Schutzfunktionen. Dadurch werden Mitarbeiter wie auch Verantwortliche optimal geschützt.</p></div>
  <div class="feature" style="top:980px"><span class="plus">+</span><h3>Perfekte Oberflächen</h3><p>Selvadon bietet eine intuitive, selbsterklärende und sehr einfach zu bedienenden Oberfläche. Dies führt zu einer sehr hohen Akzeptanz und minimalem Schulungsaufwand.</p></div>
  <div class="feature" style="top:1068px"><span class="plus">+</span><h3>Transparente Prozesse</h3><p>Durch das Zusammenwirken aller Module werden Unstimmigkeiten im Arbeitsschutz automatisiert erkannt und per Dashboard dem jeweiligen Verantwortlichen gemeldet.</p></div>

  <!-- Funktionen & Module -->
  <div class="band" style="top:1260px;height:420px"></div>
  <div class="placeholder" role="img" aria-label="Foto: Hände auf einem Laptop mit geöffneter Arbeitsschutz-Software"
       style="left:514px;top:1221px;width:479px;height:405px;background:linear-gradient(135deg,#dfe6e6 0%,#b9c3c4 45%,#8d9697 100%)"></div>

  <div class="eyebrow" style="left:77px;top:1299px">Breite Palette</div>
  <h2 class="section-title" style="left:77px;top:1320px">Funktionen &amp; Module</h2>
  <p class="body-text" style="left:77px;top:1364px;width:380px">Unsere Software für Arbeitsschutz bietet eine breite Palette an Modulen und Funktionen, um Sie im Bereich Arbeitsschutz und Management bestmöglich zu unterstützen:</p>
  <ul class="module-list" style="left:77px;top:1426px">
    <li>Basisfunktionen</li><li>Gefährdungsbeurteilung</li><li>Unterweisung</li><li>Unfallmanagement</li><li>Gefahrstoffmanagement</li><li>Vorsorgeuntersuchungen</li><li>Qualifikationsmatrix</li>
  </ul>
  <ul class="module-list" style="left:274px;top:1426px">
    <li>Maßnahmenmanagement</li><li>Auditierung</li><li>Compliance</li><li>Dateiarchiv</li><li>Controlling und Management</li><li>Multilingual verfügbar</li>
  </ul>
  <div class="btn" style="left:77px;top:1595px;width:169px;height:32px">Funktionen im Detail</div>

  <!-- Kunden -->
  <div class="eyebrow center" style="top:1757px">Sie vertrauen uns</div>
  <h2 class="section-title center" style="top:1780px">Selvadon Kundenauszug</h2>
  <div class="client" style="left:194px">KALMOR</div>
  <div class="client" style="left:381px"><span class="sq"></span>TESSARO</div>
  <div class="client" style="left:557px">VARNHOLT</div>
  <div class="client" style="left:774px"><span class="dot"></span>QUENDA</div>

  <!-- Wofür steht -->
  <div class="band" style="top:2037px;height:391px"></div>
  <div class="placeholder" role="img" aria-label="Porträtfoto des Ansprechpartners im weißen Hemd"
       style="left:55px;top:2003px;width:206px;height:206px;background:linear-gradient(180deg,#dcdcdc,#a9a9a9)"></div>
  <div class="abs" style="left:20px;top:2236px;width:276px;text-align:center">
    <div style="font-size:18px;color:#333">Jonas Brenner</div>
    <div style="font-size:13px;color:#444;margin-top:4px">Ihr persönlicher Ansprechpartner</div>
    <p style="font-size:11.5px;line-height:17px;color:#444;margin-top:19px">Nehmen Sie jetzt Kontakt auf und vereinbaren Sie Ihren unverbindlichen Beratungs- und Präsentationstermin.</p>
  </div>

  <div class="eyebrow" style="left:334px;top:2082px">Das sicherste Platz</div>
  <h2 class="section-title" style="left:334px;top:2103px">Wofür steht Selvadon?</h2>
  <p class="body-text" style="left:334px;top:2146px;width:560px">Als „Pretorium“ wurde in einem römischen Legionslager das Zelt des Befehlshabers bezeichnet – der sicherste Platz im Lager. Prätorianer gehörten der kaiserlichen Gardetruppe an, die das Pretorium beschützt haben. Arbeitsschützer sind die heutigen Prätorianer die das Unternehmen vor Gefahren und Unfällen beschützen.</p>
  <p class="body-text" style="left:334px;top:2212px;width:560px">Selvadon wird gemeinsam mit unserem Kompetenzteam entwickelt. Zum Kompetenzteam gehören viele Fachkräfte für Arbeitssicherheit die in den Unternehmen direkt an der Basis arbeiten – bis hin zu hochqualifizierten Beratern und Autoren. Diese Mischung macht unsere Software so perfekt, da Sie exakt die Wünsche, Bedürfnisse und Funktionen abbildet, die jeden Tag in den Unternehmen benötigt werden.</p>
  <div class="btn" style="left:334px;top:2320px;width:261px;height:38px">Präsentationstermin vereinbaren</div>

  <!-- Footer -->
  <footer class="footer">
    <div class="brand" style="left:72px;top:52px;font-size:13px;flex-direction:column;gap:10px">
      <span class="mark" style="width:34px;height:34px"></span>
      <span>SELVADON</span>
    </div>
    <p class="abs" style="left:74px;top:148px;width:200px;font-size:11px;line-height:16.6px;color:#3f4a38">Lorem ipsum dolor sit amet, dolor consectetur adipiscing elit. Sit amet, consectetur adipiscing elit.</p>
    <div class="f-col" style="left:355px"><h4>ARBEITSSCHUTZ SOFTWARE MODULE</h4>Basisfunktionen<br>Gefährdungsbeurteilung<br>Unterweisung<br>Unfallmanagement<br>Gefahrstoffmanagement<br>Auditierung<br>Compliance</div>
    <div class="f-col" style="left:613px"><h4>INFORMATIONEN</h4>Unternehmen<br>Präsentationstermin<br>Kontakt</div>
    <div class="f-col" style="left:794px"><h4>RECHTLICHES</h4>AGB<br>Datenschutz<br>Cookies<br>Impressum</div>
  </footer>
  <div class="footer-bar">
    <span class="abs" style="left:47px;top:24px">© 2022 • Selvadon • Nordwerk Docs GmbH</span>
    <span class="abs" style="left:716px;top:24px">UNSER PARTNER</span>
    <span class="abs" style="left:818px;top:16px;width:30px;height:30px;border-radius:50%;background:#8cc46a"></span>
    <span class="abs" style="left:857px;top:20px;font-size:11px">klare wege</span>
  </div>
</div>
</body>
</html>
```